New Townhome community needs for sale sign.

need a 4 foot by 8 foot banner to put on building listing newly constructed townhomes as "coming soon" to market. Construction is scheduled to be completed Dec 2024. Sale of units will begin Spring of 2025.
6 individual townhome units each 2,000 square feet. each unit is 3 bedroom 2.5 bathroom with 2 car garage and each has a rooftop "sky lounge" with amazing views. Gated community. Units available for sale Spring of 2025. Real estate company selling units will be KTL & Associates. Will need KTL & Associates Logo on the banner. Would like to keep with the same blue color scheme as the KTL & Associates logo. phone number on banner to be 480-555-3164. web ktlpartners.example.

```html
<!DOCTYPE html>
<html lang="en">
<head>
<meta charset="utf-8">
<title>KTL &amp; Associates – Townhomes Coming Soon</title>
<link href="https://fonts.googleapis.com/css2?family=Open+Sans:wght@400;600&family=Oswald:wght@600&display=swap" rel="stylesheet">
<style>
  :root {
    --page: #ffffff;
    --banner: #def0f8;
    --navy: #1c6e9c;
    --sky: #24a6d6;
    --ink: #333333;
    --white: #ffffff;
  }
  * { margin: 0; padding: 0; box-sizing: border-box; }
  html, body { width: 1200px; height: 1000px; overflow: hidden; background: var(--page); }
  body { position: relative; font-family: "Open Sans", sans-serif; }

  .banner {
    position: absolute; left: 383px; top: 67px; width: 433px; height: 866px;
    background: var(--banner); color: var(--navy);
  }
  .banner > * { position: absolute; }

  .headline {
    left: 29px; top: -6px; font-size: 118px; line-height: 1; letter-spacing: -3px; font-weight: 400;
  }

  .ribbon { left: 277px; top: 0; width: 124px; height: 124px; }
  .ribbon-text {
    left: 277px; top: 43px; width: 124px; text-align: center; color: var(--white);
    font-size: 26px; line-height: 30px;
  }

  .title {
    left: 32px; top: 156px; font-family: "Oswald", sans-serif; font-weight: 600;
    font-variant: small-caps; color: var(--sky); font-size: 52px; line-height: 49px;
    letter-spacing: 0.5px; transform: scaleX(0.92); transform-origin: left;
  }

  .date-box {
    left: 277px; width: 125px; border: 2px solid var(--navy); text-align: center;
  }
  .date-box .label { background: var(--navy); color: var(--white); }
  .completion { top: 168px; height: 132px; }
  .completion .label { font-size: 17px; line-height: 22px; padding: 3px 0 4px; }
  .completion .month { font-size: 22px; line-height: 28px; margin-top: 2px; }
  .completion .year { font-size: 48px; line-height: 48px; }
  .sales { top: 352px; height: 132px; }
  .sales .label { font-size: 18px; line-height: 30px; }
  .sales .season { font-size: 34px; line-height: 44px; margin-top: 2px; }
  .sales .year { font-size: 48px; line-height: 48px; }

  .summary {
    left: 32px; top: 342px; width: 170px; font-size: 26px; line-height: 30px;
  }

  .features-bar {
    left: 32px; top: 522px; width: 369px; height: 41px; background: var(--navy);
    color: var(--white); font-size: 28px; line-height: 41px; padding-left: 11px;
  }

  .features-list { top: 579px; list-style: none; font-size: 19px; line-height: 25px; }
  .features-list li { position: relative; padding-left: 18px; }
  .features-list li::before {
    content: ""; position: absolute; left: 0; top: 10px; width: 6px; height: 6px; background: var(--sky);
  }
  .col-a { left: 32px; }
  .col-b { left: 196px; width: 210px; }

  .brand {
    left: 32px; top: 752px; width: 369px; display: flex; align-items: center; gap: 12px;
  }
  .brand-mark { width: 34px; height: 34px; background: var(--navy); flex: none; }
  .brand-name { font-size: 34px; font-weight: 600; color: var(--ink); letter-spacing: -0.5px; white-space: nowrap; }

  .phone {
    left: 0; top: 788px; width: 433px; text-align: center; color: var(--ink);
    font-size: 32px; letter-spacing: 1.5px; line-height: 40px;
  }
  .web {
    left: 0; top: 827px; width: 433px; text-align: center; color: var(--ink);
    font-size: 21px; letter-spacing: 1px; line-height: 28px;
  }
</style>
</head>
<body>
  <section class="banner">
    <h1 class="headline">Sale!</h1>

    <svg class="ribbon" viewBox="0 0 124 124" aria-hidden="true">
      <polygon points="0,0 124,0 124,95 62,124 0,95" fill="var(--navy)"/>
    </svg>
    <p class="ribbon-text">Coming<br>Soon</p>

    <h2 class="title">Individual<br>Townhome<br>Units</h2>

    <div class="date-box completion">
      <div class="label">Construction<br>Completion</div>
      <div class="month">December</div>
      <div class="year">2024</div>
    </div>

    <p class="summary">6 individual townhome units each 2,000 square feet.</p>

    <div class="date-box sales">
      <div class="label">Sales Begin</div>
      <div class="season">Spring</div>
      <div class="year">2025</div>
    </div>

    <h3 class="features-bar">Features</h3>
    <ul class="features-list col-a">
      <li>3 bedrooms</li>
      <li>2.5 bathrooms</li>
      <li>2-car garage</li>
    </ul>
    <ul class="features-list col-b">
      <li>Rooftop “sky lounge” with amazing views</li>
      <li>Gated community</li>
    </ul>

    <div class="brand">
      <span class="brand-mark" aria-hidden="true"></span>
      <span class="brand-name">KTL &amp; Associates</span>
    </div>
    <p class="phone">480-555-3164</p>
    <p class="web">www.ktlpartners.example</p>
  </section>
</body>
</html>
```